Need a banner made for my LinkedIn Profile

We are a sell side advisor and we need to update our LinkedIn banner
Copper Ridge offers two services:
1. Sell Side Advisory
2. And through our TetherMark program, Exit Readiness

Target Market(s)

Business owners, Private Equity Firms

Industry/Entity Type

Mergers and Acquisitions

Logo Text

Sell-Side Advisory Exit-Readiness

Font styles to use
Other font styles liked:
• Match logo fonts

Colors

Designer to choose colors to be used in the design.

Requirements
Must have
• Use the colors on the Copper Ridge Logo-All white background, use both logos

```html
<!DOCTYPE html>
<html lang="en">
<head>
<meta charset="utf-8">
<title>LinkedIn Banner - Design 1</title>
<link href="https://fonts.googleapis.com/css2?family=Poppins:ital,wght@0,400;0,600;0,700;1,700&display=swap" rel="stylesheet">
<style>
  :root {
    --navy: #033f5c;
    --ink: #082b4c;
    --teal: #2c8a9e;
    --aqua: #85d0dc;
    --mist: #eff3f6;
    --frame: #3c6680;
    --paper: #fefefe;
    --white: #ffffff;
  }
  * { margin: 0; padding: 0; box-sizing: border-box; }
  html, body {
    width: 1200px; height: 1200px; overflow: hidden;
    background: var(--paper);
    font-family: "Poppins", sans-serif;
    color: var(--ink);
  }
  .board { position: relative; width: 1200px; height: 1200px; }
  .board-title {
    position: absolute; left: 62px; top: 456px;
    font-size: 25px; font-weight: 400; letter-spacing: 0.2px;
  }
  .banner {
    position: absolute; left: 62.5px; top: 512.5px;
    width: 1081px; height: 183px;
    border: 0.6px solid var(--frame);
    background: var(--white);
    overflow: hidden;
  }
  .banner-bg { position: absolute; inset: 0; width: 100%; height: 100%; }
  .backdrop-art {
    position: absolute; left: 819px; top: 0; width: 262px; height: 183px;
    background: linear-gradient(100deg, rgba(239,243,246,0) 0%, var(--mist) 55%, var(--mist) 100%);
  }
  .brand {
    position: absolute; left: 178px; top: 47px;
    display: flex; align-items: center; gap: 16px;
  }
  .brand-dot {
    width: 90px; height: 90px; border-radius: 50%;
    background: var(--white);
  }
  .brand-name {
    color: var(--white); font-size: 31px; font-weight: 600;
    letter-spacing: -0.6px; white-space: nowrap;
  }
  .services {
    position: absolute; left: 733px; top: 24px;
  }
  .services-lead {
    font-size: 19px; font-weight: 700; font-style: italic;
    line-height: 20px; letter-spacing: -0.2px;
  }
  .services-sub { font-size: 17px; line-height: 22px; margin-top: 1px; }
  .service-list { list-style: none; margin-top: 17px; }
  .service-item {
    position: relative; font-size: 17.5px; line-height: 20px;
    margin-bottom: 9px;
  }
  .service-item::before {
    content: ""; position: absolute; left: -14px; top: 7px;
    border-left: 6px solid var(--ink);
    border-top: 3.5px solid transparent;
    border-bottom: 3.5px solid transparent;
  }
</style>
</head>
<body>
<main class="board">
  <h1 class="board-title">LinkedIn Banner - Design 1</h1>

  <section class="banner">
    <svg class="banner-bg" viewBox="0 0 1081 183" preserveAspectRatio="none" aria-hidden="true">
      <polygon points="0,0 687.5,0 540.6,183 0,183" fill="var(--navy)"/>
      <polygon points="687.5,0 712.5,0 565.6,183 540.6,183" fill="var(--teal)"/>
      <polygon points="712.5,0 736,0 589.4,183 565.6,183" fill="var(--aqua)"/>
    </svg>

    <div class="backdrop-art" role="img" aria-label="Faint brand mountain decoration"></div>

    <div class="brand">
      <span class="brand-dot"></span>
      <span class="brand-name">Copper Ridge Capital</span>
    </div>

    <div class="services">
      <p class="services-lead">Copper Ridge Capital</p>
      <p class="services-sub">offers two services:</p>
      <ul class="service-list">
        <li class="service-item">Sell Side Advisory</li>
        <li class="service-item">TetherMark program,<br>Exit Readiness</li>
      </ul>
    </div>
  </section>
</main>
</body>
</html>
```